Construction machinery rental / heavy equipment rental needs a nice billboard

We need a billboard for our company.
We rent out construction machinery such as excavators, wheel loaders, wheel dumpers and so on...

I would like an elegant, simple, dark design.
Colors: black yellow grey white

The following must be on the billboard:
Logo
phone number: 078 / 513 90 41
website: www.kiesgrube-talwerk.ch
the machines I rent out: Bagger bis 10T, Radlader, Dumper, Raupenkipper

the font in the logo is: Square 721

Final format 2950 x 1900mm
I have uploaded pictures:
"Excavator 1-6" are my pictures, which can be used
"Sample 1-4" are pictures whose style I like
"Billboard" are billboards which I like

Requirements
Must have
• The following must be on the billboard: Logo phone number: 078 / 513 90 41 website: www.kiesgrube-talwerk.ch the machines I rent out: Bagger bis 10T, Radlader, Dumper, Raupenkipper

```html
<!DOCTYPE html>
<html lang="de">
<head>
<meta charset="utf-8">
<title>Talwerk Baumaschinenvermietung – Plakat</title>
<link href="https://fonts.googleapis.com/css2?family=Poppins:wght@700;800&family=Exo+2:ital,wght@1,800&display=swap" rel="stylesheet">
<style>
  :root {
    --black: #060708;
    --yellow: #e2c84a;
    --line-yellow: #f2e21a;
    --white: #ffffff;
    --grey-dark: #2a2b2d;
    --grey-light: #9a9ca0;
  }
  * { margin: 0; padding: 0; box-sizing: border-box; }
  html, body { width: 1200px; height: 870px; overflow: hidden; background: var(--black); }
  .billboard {
    position: relative;
    width: 1200px;
    height: 870px;
    background: var(--black);
    font-family: "Poppins", Arial, sans-serif;
    color: var(--white);
    overflow: hidden;
  }
  .brand {
    position: absolute;
    left: 80px;
    top: 110px;
    display: flex;
    align-items: center;
    gap: 18px;
    color: var(--yellow);
    font-weight: 800;
  }
  .brand-mark {
    width: 58px;
    height: 58px;
    background: var(--yellow);
  }
  .brand-name { font-size: 70px; line-height: 0.95; letter-spacing: 2px; }
  .brand-sub { font-size: 21px; line-height: 1.3; letter-spacing: 1.5px; }
  .tagline-band {
    position: absolute;
    left: 0;
    top: 262px;
    width: 592px;
    height: 63px;
    background: var(--yellow);
    clip-path: polygon(0 0, 100% 0, 97% 100%, 0 100%);
  }
  .tagline {
    position: absolute;
    left: 70px;
    top: 0;
    line-height: 63px;
    font-family: "Exo 2", Arial, sans-serif;
    font-style: italic;
    font-weight: 800;
    font-size: 37px;
    color: var(--black);
    white-space: nowrap;
  }
  .machine-list {
    position: absolute;
    left: 134px;
    top: 374px;
    width: 345px;
    list-style: none;
    text-align: center;
  }
  .machine-list li {
    font-weight: 700;
    font-size: 28px;
    letter-spacing: 1px;
    height: 56px;
    line-height: 44px;
    position: relative;
  }
  .machine-list li:not(:last-child)::after {
    content: "";
    position: absolute;
    left: 0; right: 0; bottom: 5px;
    height: 2px;
    background: linear-gradient(90deg, transparent, var(--line-yellow) 20%, var(--line-yellow) 80%, transparent);
  }
  .machine-photo {
    position: absolute;
    left: 659px;
    top: 74px;
    width: 541px;
    height: 560px;
    background: radial-gradient(ellipse at 60% 45%, var(--grey-light) 0%, var(--grey-dark) 45%, var(--black) 75%);
  }
  .contact-phone {
    position: absolute;
    left: 70px;
    top: 648px;
    display: flex;
    align-items: center;
    gap: 38px;
  }
  .phone-icon { width: 88px; height: 93px; }
  .phone-number {
    font-weight: 800;
    font-size: 124px;
    line-height: 1;
    letter-spacing: 4px;
    white-space: nowrap;
  }
  .web-band {
    position: absolute;
    left: 15px;
    top: 783px;
    width: 1167px;
    height: 75px;
    background: var(--yellow);
    display: flex;
    align-items: center;
    justify-content: center;
  }
  .web-address {
    font-weight: 800;
    font-size: 44px;
    letter-spacing: 13px;
    color: var(--black);
  }
</style>
</head>
<body>
<main class="billboard">
  <div class="brand">
    <div class="brand-mark"></div>
    <div>
      <div class="brand-name">TALWERK</div>
      <div class="brand-sub">BAUMASCHINENVERMIETUNG</div>
    </div>
  </div>

  <div class="tagline-band">
    <span class="tagline">THE MACHINES I RENT OUT</span>
  </div>

  <ul class="machine-list">
    <li>BAGGER BIS 10T</li>
    <li>RADLADER</li>
    <li>DUMPER</li>
    <li>RAUPENKIPPER</li>
  </ul>

  <div class="machine-photo" role="img" aria-label="Schwarzweiss-Foto eines Mobilbaggers mit grossen Rädern, von unten beleuchtet"></div>

  <div class="contact-phone">
    <svg class="phone-icon" viewBox="0 0 88 93" aria-hidden="true">
      <rect x="0" y="0" width="88" height="93" rx="12" fill="var(--yellow)"/>
      <rect x="11" y="11" width="66" height="71" rx="7" fill="none" stroke="var(--black)" stroke-width="3"/>
      <path d="M30 24 l8 -3 l6 12 l-5 4 c2 6 6 11 12 14 l4 -5 l12 6 l-3 8 c-18 2 -36 -16 -34 -36 z" fill="none" stroke="var(--black)" stroke-width="3" stroke-linejoin="round"/>
      <g fill="var(--black)">
        <circle cx="22" cy="48" r="1.6"/><circle cx="24" cy="54" r="1.6"/><circle cx="27" cy="60" r="1.6"/>
        <circle cx="31" cy="65" r="1.6"/><circle cx="36" cy="69" r="1.6"/><circle cx="42" cy="72" r="1.6"/>
      </g>
    </svg>
    <span class="phone-number">078 / 513 90 41</span>
  </div>

  <div class="web-band">
    <span class="web-address">www.kiesgrube-talwerk.ch</span>
  </div>
</main>
</body>
</html>
```